General Dental Office Business Card

I run a private general dental office in southern California, and would like a refresh/redesign of my business card. I focus on quality care rather than volume. The email address on the uploaded current card should be updated to: info@marbleshoredental.example. The current card's logo is a deboss, but I am open to other ideas. The logo can be refreshed, but it is something that's been with me since the beginning of the office, so I wouldn't want a drastic redesign.
Target Market(s)
Adults 18-99, whoever needs dental services
Industry/Entity Type
Healthcare/Dental
Contact Information for Business Card
Name, Address, Phone, email
Colors
Designer to choose colors to be used in the design.
Requirements
Must have
- Logo (Same as original one in the uploaded file), space on back for appointment time/date

```html
<!DOCTYPE html>
<html lang="en">
<head>
<meta charset="UTF-8">
<title>Marble Shore Dental – Business Card</title>
<link rel="stylesheet" href="https://fonts.googleapis.com/css2?family=Montserrat:wght@500;600;700&display=swap">
<style>
  :root {
    --backdrop: #cfe7f1;
    --sky: #7ccadf;
    --paper: #ffffff;
    --mark-pale: #d5ebf3;
    --ink: #4d4d4d;
    --rule: #6b6b6b;
  }
  * { box-sizing: border-box; margin: 0; padding: 0; }
  html, body {
    width: 1200px; height: 1200px; overflow: hidden;
    background: var(--backdrop);
    font-family: "Montserrat", Arial, sans-serif;
  }
  .sheet {
    width: 1200px; height: 1200px;
    display: flex; align-items: center; justify-content: center; gap: 80px;
  }
  .card {
    position: relative;
    width: 400px; height: 700px;
    background: var(--paper);
    overflow: hidden;
    box-shadow: 0 6px 18px rgba(60, 110, 130, 0.18);
  }
  .card__waves { position: absolute; left: 0; top: 0; width: 400px; height: 700px; }

  /* front */
  .brand-mark {
    position: absolute; left: 0; right: 0; top: 250px;
    display: flex; flex-direction: column; align-items: center; gap: 14px;
  }
  .brand-mark__disc { width: 150px; height: 150px; border-radius: 50%; background: var(--mark-pale); }
  .brand-mark__name { font-weight: 600; font-size: 18px; color: var(--sky); }
  .front .brand-mark__name { color: #a9d9e7; }

  .identity {
    position: absolute; right: 34px; left: 34px; top: 458px;
    text-align: right;
  }
  .identity__name { font-weight: 700; font-size: 25px; color: var(--sky); letter-spacing: 0.2px; }
  .identity__role { font-weight: 500; font-size: 15px; color: var(--sky); margin-top: 2px; }
  .identity__rule { border: 0; border-top: 1px solid var(--rule); margin: 12px 0 14px; }
  .contact { font-weight: 600; font-size: 13px; color: var(--ink); line-height: 1.45; }
  .contact p + p { margin-top: 8px; }

  /* back */
  .back { background: var(--sky); }
  .back .brand-mark { top: 240px; }
  .back .brand-mark__disc { background: var(--paper); }
  .back .brand-mark__name { color: var(--paper); }
  .appointment {
    position: absolute; left: 34px; right: 34px; top: 520px;
    color: var(--paper); font-weight: 700; font-size: 13px;
  }
  .appointment__field { display: flex; align-items: flex-end; gap: 10px; margin-bottom: 26px; }
  .appointment__line { flex: 1; border-bottom: 1.5px solid var(--paper); height: 1px; }
  .practice-name {
    position: absolute; left: 0; right: 0; bottom: 56px;
    text-align: center; color: var(--paper); font-weight: 600; font-size: 22px;
  }
</style>
</head>
<body>
<main class="sheet">

  <section class="card front" aria-label="Card front">
    <svg class="card__waves" viewBox="0 0 400 700" aria-hidden="true">
      <path d="M0 0 H400 V110 C320 80 290 150 200 140 C110 130 80 190 0 180 Z" fill="var(--sky)"/>
      <g fill="none" stroke="var(--sky)" stroke-width="6">
        <path d="M0 194 C80 204 110 144 200 154 C290 164 320 94 400 124"/>
        <path d="M0 208 C80 218 110 158 200 168 C290 178 320 108 400 138"/>
        <path d="M0 222 C80 232 110 172 200 182 C290 192 320 122 400 152"/>
      </g>
    </svg>
    <div class="brand-mark">
      <div class="brand-mark__disc"></div>
      <span class="brand-mark__name">Marble Shore Dental</span>
    </div>
    <div class="identity">
      <h1 class="identity__name">Daniel R. Moreno DDS</h1>
      <p class="identity__role">General Dentistry</p>
      <hr class="identity__rule">
      <div class="contact">
        <p>2150 Seabright Parkway<br>Marble Shore, CA 90000</p>
        <p>555-014-2370</p>
        <p>info@marbleshoredental.example<br>www.marbleshoredental.example</p>
      </div>
    </div>
  </section>

  <section class="card back" aria-label="Card back">
    <svg class="card__waves" viewBox="0 0 400 700" aria-hidden="true">
      <path d="M0 0 H400 V110 C320 80 290 150 200 140 C110 130 80 190 0 180 Z" fill="var(--paper)"/>
      <g fill="none" stroke="var(--paper)" stroke-width="6">
        <path d="M0 187 C80 197 110 137 200 147 C290 157 320 87 400 117"/>
        <path d="M0 201 C80 211 110 151 200 161 C290 171 320 101 400 131"/>
        <path d="M0 215 C80 225 110 165 200 175 C290 185 320 115 400 145"/>
      </g>
      <g fill="none" stroke="var(--sky)" stroke-width="7">
        <path d="M0 193 C80 203 110 143 200 153 C290 163 320 93 400 123"/>
        <path d="M0 207 C80 217 110 157 200 167 C290 177 320 107 400 137"/>
      </g>
    </svg>
    <div class="brand-mark">
      <div class="brand-mark__disc"></div>
    </div>
    <div class="appointment">
      <div class="appointment__field"><span>Appointment Date</span><span class="appointment__line"></span></div>
      <div class="appointment__field"><span>Time</span><span class="appointment__line"></span></div>
    </div>
    <p class="practice-name">Marble Shore Dental</p>
  </section>

</main>
</body>
</html>
```